1/2 Page add for BRMTL Conference

We are looking for a 1/2 page ad to support the annual BRMTL conference. I want to encourage the attendees to come to our both so we can explain how they can save money on food and supplies. here is a link to the conference. https://www.brmtl-example.org/conference/ here is our website www.pantrywisehub-example.com - the what we do can be captured in the ad. We will be at booth 505. Our goal is to get people to our booth #505 to explain the services that we provide –

Discounted food pricing
Free menu planning/design
Use of Registered Dietitian
Huge selection of discounted PPE and other necessary supplies to run any child care center

We have over 6000 members in 46 States and work with both small and large food distributors. We have been a sponsor of the association for the last 10 years.

Target Market(s)

Child care centers

Requirements
Must have
• Booth number -outline of what we do --- Stress we are a FREE service getting our members reduced pricing on food and supplies

```html
<!DOCTYPE html>
<html lang="en">
<head>
<meta charset="utf-8">
<title>BRMTL Conference Half-Page Ad – PantryWise Hub</title>
<link rel="stylesheet" href="https://fonts.googleapis.com/css2?family=Montserrat:wght@600;700;800&family=Yellowtail&display=swap">
<style>
  :root {
    --leaf-green: #8fc886;
    --brand-blue: #3c7cc2;
    --white: #ffffff;
    --ink-gray: #6b6e72;
    --page-bg: #ffffff;
  }
  html, body {
    margin: 0;
    padding: 0;
    width: 1200px;
    height: 1000px;
    overflow: hidden;
    background: var(--page-bg);
  }
  .ad {
    position: absolute;
    left: 85px;
    top: 167px;
    width: 1030px;
    height: 665px;
    background: var(--leaf-green);
    overflow: hidden;
    font-family: "Montserrat", sans-serif;
    color: var(--white);
    box-shadow: 0 1px 4px rgba(0,0,0,0.12);
  }
  .ad-shapes {
    position: absolute;
    left: 0;
    top: 0;
  }
  .eyebrow {
    position: absolute;
    left: 0;
    width: 560px;
    top: 26px;
    text-align: center;
    font-size: 25px;
    font-weight: 700;
    letter-spacing: 0.5px;
    margin: 0;
    white-space: nowrap;
  }
  .headline {
    position: absolute;
    left: 32px;
    width: 494px;
    top: 62px;
    margin: 0;
    text-align: center;
    font-size: 58px;
    font-weight: 800;
    letter-spacing: 0;
    white-space: nowrap;
    color: var(--brand-blue);
    line-height: 1;
    padding-bottom: 8px;
    border-bottom: 3px solid var(--brand-blue);
  }
  .service-list {
    position: absolute;
    left: 36px;
    top: 155px;
    margin: 0;
    padding: 0;
    list-style: none;
    font-size: 25px;
    font-weight: 700;
    line-height: 41px;
    white-space: nowrap;
  }
  .service-list li {
    position: relative;
    padding-left: 39px;
    margin-bottom: 9px;
  }
  .service-list .tick {
    position: absolute;
    left: 0;
    top: 14px;
    width: 14px;
    height: 12px;
  }
  .booth-cta {
    position: absolute;
    left: 0;
    top: 0;
    width: 560px;
    height: 665px;
    margin: 0;
    text-align: center;
  }
  .booth-cta span {
    position: absolute;
    left: 0;
    width: 560px;
    white-space: nowrap;
  }
  .booth-cta .invite {
    top: 462px;
    font-family: "Yellowtail", cursive;
    font-size: 56px;
    line-height: 1;
  }
  .booth-cta .booth-number {
    top: 527px;
    font-size: 76px;
    font-weight: 700;
    line-height: 1;
    letter-spacing: 1px;
  }
  .booth-cta .follow-up {
    top: 608px;
    font-size: 25px;
    font-weight: 700;
    line-height: 1.2;
  }
  .brand-card {
    position: absolute;
    left: 733px;
    top: 561px;
    width: 297px;
    height: 104px;
    background: var(--white);
    color: var(--ink-gray);
  }
  .brand-name {
    position: absolute;
    left: 18px;
    top: 22px;
    display: flex;
    align-items: center;
    gap: 10px;
    font-size: 22px;
    font-weight: 600;
    margin: 0;
    white-space: nowrap;
  }
  .brand-name .mark {
    width: 28px;
    height: 28px;
    background: var(--brand-blue);
  }
  .brand-url {
    position: absolute;
    left: 0;
    width: 297px;
    top: 75px;
    text-align: center;
    font-size: 14px;
    font-weight: 700;
    margin: 0;
    white-space: nowrap;
  }
</style>
</head>
<body>
<main class="ad">
  <svg class="ad-shapes" width="1030" height="665" viewBox="0 0 1030 665">
    <defs>
      <linearGradient id="fruit-tones" x1="0" y1="0" x2="1" y2="1">
        <stop offset="0" stop-color="#c9d46a"/>
        <stop offset="0.5" stop-color="#d9892e"/>
        <stop offset="1" stop-color="#8a2a2a"/>
      </linearGradient>
      <linearGradient id="portrait-tones" x1="0" y1="0" x2="1" y2="1">
        <stop offset="0" stop-color="#e7cdb3"/>
        <stop offset="0.6" stop-color="#d2a884"/>
        <stop offset="1" stop-color="#a4876b"/>
      </linearGradient>
    </defs>
    <rect class="cta-band" x="0" y="445" width="680" height="220" fill="var(--brand-blue)"/>
    <circle class="fruit-photo" cx="773" cy="133" r="222" fill="url(#fruit-tones)" stroke="var(--white)" stroke-width="4" role="img" aria-label="Photo of fresh fruit: grapes, pineapple, mango and plums"/>
    <circle class="child-photo" cx="900" cy="483" r="302" fill="url(#portrait-tones)" stroke="var(--white)" stroke-width="5" role="img" aria-label="Photo of a smiling young child resting her chin on her hands"/>
  </svg>

  <p class="eyebrow">WE PROVIDE A</p>
  <h1 class="headline">FREE SERVICE</h1>

  <ul class="service-list">
    <li><svg class="tick" viewBox="0 0 14 12"><path d="M1 6 L5 10 L13 1" fill="none" stroke="#fff" stroke-width="2.5"/></svg>Discounted food pricing</li>
    <li><svg class="tick" viewBox="0 0 14 12"><path d="M1 6 L5 10 L13 1" fill="none" stroke="#fff" stroke-width="2.5"/></svg>Free menu planning/design</li>
    <li><svg class="tick" viewBox="0 0 14 12"><path d="M1 6 L5 10 L13 1" fill="none" stroke="#fff" stroke-width="2.5"/></svg>Use of Registered Dietitian</li>
    <li><svg class="tick" viewBox="0 0 14 12"><path d="M1 6 L5 10 L13 1" fill="none" stroke="#fff" stroke-width="2.5"/></svg>Huge selection of discounted<br>PPE and other necessary supplies<br>to run any child care center</li>
  </ul>

  <p class="booth-cta">
    <span class="invite">Visit us at</span>
    <span class="booth-number">BOOTH # 505</span>
    <span class="follow-up">to learn more about our services!</span>
  </p>

  <div class="brand-card">
    <p class="brand-name"><span class="mark"></span>PantryWise Hub</p>
    <p class="brand-url">www.pantrywisehub-example.com</p>
  </div>
</main>
</body>
</html>
```